He Lanternway Ridge Podcast is a Top Rated Show dedicated to improving the lives of our brave men and women who serve. Topics about leadership, mental health & resiliency to start living your best life personally and professionally.

Target Market(s)

First Responder Community - Law Enforcement, EMS, Fire Department, Military

Industry/Entity Type

First Responder Community

Requirements
Must have
• I would like my picture and logo to be part of the design. This needs to be formatted for Quillbeam Casts and other platforms
Nice to have
• Some style. Modern Look
Should not have
• N/A

```html
<!DOCTYPE html>
<html lang="en">
<head>
<meta charset="utf-8">
<title>Lanternway Ridge Podcast – Cover Art</title>
<link rel="stylesheet" href="https://fonts.googleapis.com/css2?family=Bebas+Neue&family=Oswald:wght@300;500;700&family=Barlow:wght@400;600&display=swap">
<style>
  :root {
    --page-bg: #ffffff;
    --cover-dark: #1a120d;
    --cover-warm: #4a3426;
    --accent-blue: #0aa6f5;
    --accent-blue-deep: #0a5fa8;
    --text-light: #ffffff;
    --shirt-blue: #1d4f9a;
    --shirt-shadow: #0f2a58;
  }
  * { margin: 0; padding: 0; box-sizing: border-box; }
  html, body {
    width: 1200px; height: 843px; overflow: hidden;
    background: var(--page-bg);
  }
  .canvas {
    position: relative; width: 1200px; height: 843px;
    display: flex; align-items: center; justify-content: center;
  }
  .cover {
    position: relative; width: 800px; height: 800px; overflow: hidden;
    background: radial-gradient(ellipse at 68% 40%, var(--cover-warm) 0%, #2e2018 45%, var(--cover-dark) 100%);
    color: var(--text-light);
  }
  .host-photo {
    position: absolute; right: 0; top: 40px; width: 400px; height: 760px;
    background:
      radial-gradient(ellipse 90px 110px at 52% 14%, rgba(150,105,80,0.55), transparent 75%),
      radial-gradient(ellipse 210px 320px at 52% 52%, var(--shirt-blue), var(--shirt-shadow) 70%, transparent 100%),
      linear-gradient(180deg, transparent 80%, rgba(8,8,10,0.9) 100%);
  }
  .brand {
    position: absolute; left: 49px; top: 59px; width: 371px;
  }
  .brand-name {
    display: flex; align-items: center; gap: 12px;
    height: 51px; padding-left: 4px;
    font-family: "Oswald", sans-serif; font-weight: 700;
    font-size: 38px; letter-spacing: 2px; color: var(--text-light);
    white-space: nowrap;
  }
  .brand-mark { width: 16px; height: 16px; background: var(--accent-blue); flex: none; }
  .brand-tagline {
    margin-top: 8px;
    font-family: "Barlow", sans-serif; font-weight: 600;
    font-size: 11px; letter-spacing: 0.6px; white-space: nowrap;
  }
  .brand-tagline .dot { color: var(--accent-blue); }

  .title { position: absolute; left: 49px; top: 0; width: 330px; height: 495px; font-weight: normal; }
  .title-top, .title-bottom {
    position: absolute; left: 0; white-space: nowrap;
    font-family: "Bebas Neue", sans-serif; line-height: 1;
    transform-origin: left top;
  }
  .title-top {
    top: 168px; font-size: 62px; letter-spacing: -0.5px;
    transform: scaleY(1.45);
  }
  .title-rule {
    position: absolute; left: 0; top: 264px; width: 330px; height: 4px;
    background: var(--text-light);
  }
  .title-middle {
    position: absolute; left: 2px; top: 276px; width: 326px;
    display: flex; justify-content: space-between;
    font-family: "Oswald", sans-serif; font-weight: 300;
    font-size: 38px; line-height: 1.1;
  }
  .title-bottom {
    top: 324px; font-size: 120px; letter-spacing: 0.5px;
    transform: scaleY(1.42);
    background: linear-gradient(180deg, var(--accent-blue) 0%, var(--accent-blue) 46%, #0b3e6e 58%, var(--accent-blue) 100%);
    -webkit-background-clip: text; background-clip: text; color: transparent;
  }

  .rating-band { position: absolute; left: 0; top: 497px; width: 400px; height: 151px; }
  .rating-band svg { position: absolute; inset: 0; }
  .rating-label {
    position: absolute; left: 54px; top: 60px; width: 286px; text-align: center;
    font-family: "Bebas Neue", sans-serif; font-size: 42px; letter-spacing: 0.5px;
  }
  .topics {
    position: absolute; left: 49px; top: 678px; width: 340px;
    font-family: "Barlow", sans-serif; font-size: 18px; line-height: 1.3;
  }
  .topics strong { color: var(--accent-blue); font-weight: 600; }
</style>
</head>
<body>
<div class="canvas">
  <section class="cover">
    <div class="host-photo" role="img" aria-label="Portrait of the host, standing in a blue button-down shirt against a warm brown backdrop"></div>

    <header class="brand">
      <div class="brand-name"><span class="brand-mark"></span>LANTERNWAY RIDGE</div>
      <div class="brand-tagline">LEADERSHIP <span class="dot">★</span> COACHING <span class="dot">★</span> PERSONAL DEVELOPMENT</div>
    </header>

    <h1 class="title">
      <span class="title-top">THE LANTERNWAY</span>
      <span class="title-rule"></span>
      <span class="title-middle"><span>R</span><span>I</span><span>D</span><span>G</span><span>E</span></span>
      <span class="title-bottom">PODCAST</span>
    </h1>

    <div class="rating-band">
      <svg width="400" height="151" viewBox="0 0 400 151">
        <defs>
          <linearGradient id="band-fill" x1="0" x2="1" y1="0" y2="0">
            <stop offset="0" stop-color="#0a5fa8"/>
            <stop offset="1" stop-color="#0aa6f5"/>
          </linearGradient>
        </defs>
        <path d="M0 0 H388 Q376 75 392 151 H0 Z" fill="url(#band-fill)"/>
        <path d="M100 38 H54 V118 H176 L197 128 L218 118 H340 V38 H294" fill="none" stroke="#fff" stroke-width="2.5"/>
        <path d="M178 126 L197 136 L216 126" fill="none" stroke="#fff" stroke-width="2.5"/>
        <g fill="#f5b81c" stroke="#8a5a00" stroke-width="0.8">
          <polygon transform="translate(118 38)" points="0,-16 4.7,-5 16,-5 7,2 10.5,14 0,7 -10.5,14 -7,2 -16,-5 -4.7,-5"/>
          <polygon transform="translate(158 38)" points="0,-16 4.7,-5 16,-5 7,2 10.5,14 0,7 -10.5,14 -7,2 -16,-5 -4.7,-5"/>
          <polygon transform="translate(197 38)" points="0,-16 4.7,-5 16,-5 7,2 10.5,14 0,7 -10.5,14 -7,2 -16,-5 -4.7,-5"/>
          <polygon transform="translate(236 38)" points="0,-16 4.7,-5 16,-5 7,2 10.5,14 0,7 -10.5,14 -7,2 -16,-5 -4.7,-5"/>
          <polygon transform="translate(276 38)" points="0,-16 4.7,-5 16,-5 7,2 10.5,14 0,7 -10.5,14 -7,2 -16,-5 -4.7,-5"/>
        </g>
      </svg>
      <div class="rating-label">A TOP RATED SHOW</div>
    </div>

    <p class="topics"><strong>Topics covered:</strong> leadership, mental health &amp; resiliency to start living your best life personally and professionally.</p>
  </section>
</div>
</body>
</html>
```